Brivenor Australia Company Values.

We have just completed our company purpose, beliefs and values (for the first time, we have not had these before)
We are now wanting to add images to each company value as a visual
so they are easily identified and understood for all our staff - we need them to remember the 5 Values.
We are a manufacturer of dental materials and infection control products, based in Melbourne.

What we would like:
- A Poster (that can be placed in our staff lunch rooms)
- The values to be lined up Horizontally
- Image on the top of the words
- Wording does not all need to be the same text font
- No image photographs - please use image graphics
- No images with people
- No dental related graphics

Target audience: Brivenor staff

Our Values are:
Think Big
Have a go, learn and adapt
If you're gonna do it, do it bloody well
Empower Others
Be a good human

I have uploaded some examples.

Target Market(s)

Brivenor Team members

Industry/Entity Type

Healthcare

Colors

Designer to choose colors to be used in the design.

Requirements
Must have
• Clear horizontal layout, space between each value
Should not have
• No images with humans or dental

```html
<!DOCTYPE html>
<html lang="en">
<head>
<meta charset="utf-8">
<title>Brivenor Australia – Our Values</title>
<link href="https://fonts.googleapis.com/css2?family=Poppins:wght@600;800&display=swap" rel="stylesheet">
<style>
  :root {
    --page: #ffffff;
    --poster-light: #f7f7f7;
    --poster-dark: #dedede;
    --title-top: #1f8fe6;
    --title-bottom: #0a3fb0;
    --teal: #2fb2ad;
    --teal-text: #1f7f7b;
    --purple: #6e3468;
    --purple-text: #5a2a55;
    --green: #8dc63f;
    --green-text: #5f9a24;
    --coral: #f25c5a;
    --coral-text: #e14a4a;
    --orange: #f0a12a;
    --orange-text: #f0951a;
  }
  html, body {
    margin: 0;
    width: 1018px;
    height: 1200px;
    overflow: hidden;
    background: var(--page);
  }
  .poster {
    position: absolute;
    left: 29px;
    top: 260px;
    width: 960px;
    height: 679px;
  }
  .poster svg { display: block; }
  .title {
    font-family: "Poppins", sans-serif;
    font-weight: 800;
    font-size: 66px;
    letter-spacing: 1px;
  }
  .value-label {
    font-family: "Poppins", sans-serif;
    font-weight: 600;
    font-size: 16.5px;
  }
</style>
</head>
<body>
<main class="poster">
  <svg width="960" height="679" viewBox="0 0 960 679" xmlns="http://www.w3.org/2000/svg">
    <defs>
      <radialGradient id="posterBg" cx="50%" cy="50%" r="70%">
        <stop offset="0" stop-color="var(--poster-light)"/>
        <stop offset="1" stop-color="var(--poster-dark)"/>
      </radialGradient>
      <radialGradient id="mapTone" cx="50%" cy="50%" r="50%">
        <stop offset="0" stop-color="#d2d2d2" stop-opacity="0.55"/>
        <stop offset="1" stop-color="#d2d2d2" stop-opacity="0"/>
      </radialGradient>
      <linearGradient id="titleFill" x1="0" y1="0" x2="0" y2="1">
        <stop offset="0" stop-color="var(--title-top)"/>
        <stop offset="1" stop-color="var(--title-bottom)"/>
      </linearGradient>
      <linearGradient id="tileFill" x1="0" y1="0" x2="0" y2="1">
        <stop offset="0" stop-color="#ffffff"/>
        <stop offset="1" stop-color="#d9d9d9"/>
      </linearGradient>
      <filter id="tileShadow" x="-30%" y="-30%" width="160%" height="160%">
        <feDropShadow dx="0" dy="3" stdDeviation="3" flood-color="#000" flood-opacity="0.2"/>
      </filter>
    </defs>

    <rect class="poster-bg" width="960" height="679" fill="url(#posterBg)"/>
    <ellipse class="map-area" role="img" aria-label="Dotted map of Australia" cx="500" cy="330" rx="400" ry="320" fill="url(#mapTone)"/>

    <text class="title" x="499" y="155" text-anchor="middle" fill="url(#titleFill)" stroke="#ffffff" stroke-width="4" paint-order="stroke">OUR VALUES</text>

    <!-- Think Big -->
    <g class="value value--think-big" transform="translate(204 339)">
      <rect x="-88" y="-88" width="176" height="176" rx="26" transform="rotate(45)" fill="url(#tileFill)" stroke="var(--teal)" stroke-width="15" filter="url(#tileShadow)"/>
      <rect role="img" aria-label="Icon of a lightbulb with a half-blue, half-orange brain" x="-28" y="-58" width="56" height="70" rx="12" fill="#f2b43a" opacity="0.75"/>
      <text class="value-label" y="53" text-anchor="middle" fill="var(--teal-text)">Think Big</text>
    </g>

    <!-- Do it well -->
    <g class="value value--do-it-well" transform="translate(480 324)">
      <rect x="-88" y="-88" width="176" height="176" rx="26" transform="rotate(45)" fill="url(#tileFill)" stroke="var(--purple)" stroke-width="15" filter="url(#tileShadow)"/>
      <rect role="img" aria-label="Icon of a document under a magnifying glass" x="-27" y="-64" width="54" height="60" rx="8" fill="#8b6ac2" opacity="0.7"/>
      <text class="value-label" text-anchor="middle" fill="var(--purple-text)">
        <tspan x="0" y="15">If you're</tspan>
        <tspan x="0" y="33">gonna do it,</tspan>
        <tspan x="0" y="51">do it bloody</tspan>
        <tspan x="0" y="69">well</tspan>
      </text>
    </g>

    <!-- Be a good human -->
    <g class="value value--good-human" transform="translate(754 335)">
      <rect x="-88" y="-88" width="176" height="176" rx="26" transform="rotate(45)" fill="url(#tileFill)" stroke="var(--green)" stroke-width="15" filter="url(#tileShadow)"/>
      <rect role="img" aria-label="Icon of an open hand holding a sprouting seedling" x="-42" y="-62" width="80" height="72" rx="12" fill="#e6c850" opacity="0.7"/>
      <text class="value-label" text-anchor="middle" fill="var(--green-text)">
        <tspan x="0" y="36">Be a good</tspan>
        <tspan x="0" y="55">human</tspan>
      </text>
    </g>

    <!-- Have a go -->
    <g class="value value--have-a-go" transform="translate(345 494)">
      <rect x="-88" y="-88" width="176" height="176" rx="26" transform="rotate(45)" fill="url(#tileFill)" stroke="var(--coral)" stroke-width="15" filter="url(#tileShadow)"/>
      <rect role="img" aria-label="Icon of a graduation cap on a stack of books" x="-35" y="-64" width="70" height="68" rx="10" fill="#3a8fa0" opacity="0.65"/>
      <text class="value-label" text-anchor="middle" fill="var(--coral-text)">
        <tspan x="0" y="30">Have a go,</tspan>
        <tspan x="0" y="49">learn and</tspan>
        <tspan x="0" y="68">adapt</tspan>
      </text>
    </g>

    <!-- Empower Others -->
    <g class="value value--empower" transform="translate(613 491)">
      <rect x="-88" y="-88" width="176" height="176" rx="26" transform="rotate(45)" fill="url(#tileFill)" stroke="var(--orange)" stroke-width="15" filter="url(#tileShadow)"/>
      <rect role="img" aria-label="Icon of four hands linked at the wrists in a square" x="-40" y="-62" width="80" height="76" rx="12" fill="#e9b08c" opacity="0.75"/>
      <text class="value-label" text-anchor="middle" fill="var(--orange-text)">
        <tspan x="0" y="37">Empower</tspan>
        <tspan x="0" y="57">Others</tspan>
      </text>
    </g>
  </svg>
</main>
</body>
</html>
```